Microlight Aircraft Website Project

Need a website designed, or at least a template made, that my web programmer can work with here. We are a new manufacturer of microlight aircraft & powered hang gliders. Our company name is Brisk Tern. We manufacture portable utility aircraft in the Light Sport category (formerly known as Ultralights or Microlights). Our particular design is a 2-seat powered hang glider and caters to those who want to go explore the backcountry. We are not necessarily aviation nuts, but more into the development of a flying utility vehicle for extreme exploration and expeditions. We have been importing these aircraft from 3 countries for 15 years and have supplied over 200 expedition-quality aircraft world-wide. We are now manufacturing here in the US.

Industry/Entity Type

Manufacturer

Coding

Coded - Design and coding required

```html
<!DOCTYPE html>
<html lang="en">
<head>
<meta charset="utf-8">
<title>Brisk Tern — Microlight Aircraft</title>
<link rel="stylesheet" href="https://fonts.googleapis.com/css2?family=Open+Sans:wght@300;400;600;700&family=Lato:ital,wght@0,400;0,700;1,400&display=swap">
<style>
:root{
  --sky-deep:#2f5f8e;
  --sky-mid:#6f97bd;
  --sky-light:#c9d9e8;
  --page:#f5f8fc;
  --ink:#222;
  --muted:#555;
  --blue:#1a8fc9;
  --blue-btn:#1570c0;
  --red:#e4232a;
  --navy:#1e2a3d;
  --gold:#f2b01e;
  --footer:#231f20;
  --footer-text:#9a9a9a;
  --white:#fff;
  --tile-top:#9ebfdc;
  --tile-bottom:#c3cbd0;
}
*{box-sizing:border-box;margin:0;padding:0}
html,body{width:1200px;height:2913px;overflow:hidden}
body{position:relative;background:var(--page);font-family:"Open Sans",Arial,sans-serif;color:var(--ink)}
.abs{position:absolute}

/* hero */
.hero{left:0;top:0;width:1200px;height:565px;background:linear-gradient(160deg,var(--sky-deep) 0%,var(--sky-mid) 45%,var(--sky-light) 100%)}
.logo-box{left:130px;top:33px;width:244px;height:126px;background:var(--white);display:flex;align-items:center;justify-content:center;gap:10px}
.logo-box .mark{width:18px;height:18px;background:#1f4fa8}
.logo-box .name{font-size:30px;font-weight:700;color:#1f4fa8}
.top-nav{top:38px;left:0;width:1200px}
.top-nav a{position:absolute;color:var(--white);font-size:17px;font-weight:600;text-decoration:none}
.side-nav a{position:absolute;left:184px;color:var(--white);font-size:15px;font-weight:600;text-decoration:none}
.hero-frame{left:480px;top:135px;width:280px;height:349px;border:10px solid var(--white)}
.hero-frame .photo{position:absolute;inset:0;background:linear-gradient(180deg,#3d6a94,#86a8c8)}
.hero-frame .title{position:absolute;left:18px;top:40px;font-size:40px;font-weight:300;color:var(--white);letter-spacing:1px}
.hero-frame .caption{position:absolute;left:18px;bottom:14px;width:240px;font-size:12.5px;line-height:17px;color:var(--white)}
.order-btn{left:873px;top:321px;width:226px;height:37px}
.order-btn span{position:absolute;left:42px;top:10px;color:var(--white);font-size:13px;font-weight:600}

/* welcome */
.section-title{left:0;width:1200px;text-align:center;font-size:29px;font-weight:600;color:var(--ink)}
.section-sub{left:0;width:1200px;text-align:center;font-size:13.5px;color:var(--muted);line-height:24px}
.feature{width:300px;text-align:center}
.feature svg{display:block;margin:0 auto}
.feature h3{margin-top:22px;font-size:17px;font-weight:400;color:#333}
.feature p{margin-top:14px;font-size:12px;line-height:19px;color:var(--muted)}
.feature .more{display:block;margin-top:18px;font-size:10px;color:#333}

/* gallery */
.tile{background:linear-gradient(180deg,var(--tile-top),var(--tile-bottom))}

/* about */
.about-photo{left:106px;top:1689px;width:517px;height:372px;background:linear-gradient(135deg,#e9eef3,#b9c4cf 60%,#7c8a9a)}
.about-label{left:697px;top:1745px;font-size:32px;font-weight:400;color:var(--blue)}
.about-head{left:697px;top:1817px;font-size:32px;font-weight:600;color:var(--ink)}
.about-text{left:697px;width:445px;font-size:13.5px;line-height:22px;color:var(--muted)}

/* testimonials */
.testimonials{left:0;top:2105px;width:1200px;height:337px;background:linear-gradient(90deg,#1b2638,#26344a 50%,#1b2638)}
.t-title{left:0;top:2155px;width:1200px;text-align:center;font-family:"Lato",sans-serif;font-size:21px;font-weight:700;letter-spacing:2px;color:var(--white)}
.t-rule{left:514px;top:2190px;width:172px;height:2px;background:var(--gold)}
.quote-mark{top:2215px;font-family:Georgia,serif;font-size:96px;line-height:96px;color:#7e8796}
.t-quote{left:190px;top:2228px;width:820px;text-align:center;font-family:"Lato",sans-serif;font-style:italic;font-size:15px;line-height:29px;color:var(--white)}
.t-name{left:0;top:2300px;width:1200px;text-align:center;font-family:"Lato",sans-serif;font-weight:700;font-size:15px;color:var(--gold)}
.t-role{left:0;top:2326px;width:1200px;text-align:center;font-size:12px;color:var(--white)}
.dot{top:2372px;width:12px;height:12px;border-radius:50%}

/* newsletter */
.news-label{left:110px;top:2494px;font-size:25px;font-weight:300;color:#333}
.news-label strong{font-weight:600;color:var(--ink)}
.news-input{left:573px;top:2488px;width:371px;height:47px;border-radius:24px;background:#e4e6e9;border:3px solid #d2d5d9}
.news-btn{left:983px;top:2488px;width:103px;height:47px;border-radius:24px;background:var(--blue-btn);color:var(--white);font-size:13px;text-align:center;line-height:47px}

/* footer */
.footer{left:0;top:2574px;width:1200px;height:339px;background:var(--footer)}
.f-head{top:2604px;font-size:14px;font-weight:700;letter-spacing:1px;color:var(--white)}
.f-head::after{content:"";display:block;width:80px;height:2px;margin-top:6px;background:var(--gold)}
.f-brand{left:147px;top:2656px;display:flex;align-items:center;gap:10px;font-size:20px;font-weight:700;letter-spacing:2px;color:var(--white)}
.f-brand .mark{width:18px;height:18px;background:var(--gold)}
.f-about{left:147px;top:2695px;width:310px;font-size:11.5px;line-height:20px;color:var(--footer-text)}
.f-social{left:147px;top:2760px;display:flex;gap:12px}
.f-social span{width:11px;height:11px;background:#cfcfcf}
.f-list{list-style:none;font-size:12px;color:var(--footer-text)}
.f-list li{height:30px;line-height:20px}
.f-list li::before{content:"›";margin-right:12px;color:#777}
.f-contact{left:817px;top:2656px;list-style:none;font-size:12px;color:var(--footer-text)}
.f-contact li{height:30px;display:flex;align-items:center;gap:14px}
.f-contact svg{flex:none}
.copyright{left:0;top:2856px;width:1200px;text-align:center;font-size:11px;color:#bdbdbd}
</style>
</head>
<body>

<header>
  <div class="abs hero"></div>
  <div class="abs logo-box"><span class="mark"></span><span class="name">Brisk Tern</span></div>
  <nav class="abs top-nav">
    <a style="left:735px">Experience</a>
    <a style="left:888px">Innovation</a>
    <a style="left:1039px">Support</a>
  </nav>
  <nav class="side-nav">
    <a style="top:218px">Ready To Fly</a>
    <a style="top:261px">Build &amp; Fly</a>
    <a style="top:304px">Open Cockpit</a>
    <a style="top:347px">Spare Parts</a>
    <a style="top:390px">Gallery</a>
    <a style="top:433px">About</a>
    <a style="top:476px">Contact</a>
  </nav>
  <div class="abs hero-frame">
    <div class="photo" role="img" aria-label="Red two-seat gyro microlight flying against blue sky"></div>
    <div class="title">BRISK TERN</div>
    <p class="caption">Proin risus tellus, maximus nec diam aliquet sollicitudin massa.</p>
  </div>
  <div class="abs order-btn">
    <svg width="226" height="37" viewBox="0 0 226 37"><polygon points="0,0 226,0 206,37 0,37" fill="var(--red)"/><path d="M138 19h22m-6-5 6 5-6 5" stroke="#fff" stroke-width="2" fill="none"/></svg>
    <span>ORDER NOW</span>
  </div>
</header>

<section class="welcome">
  <h1 class="abs section-title" style="top:612px">WELCOME TO BRISK TERN</h1>
  <p class="abs section-sub" style="top:663px">DONEC VITAE RHONCUS EX. NULLA PORTTITOR, LIGULA ID SUSCIPIT VESTIBULUM</p>

  <div class="abs feature" style="left:92px;top:758px">
    <svg width="42" height="42" viewBox="0 0 42 42" fill="none" stroke="#1a6fb5" stroke-width="2"><circle cx="21" cy="21" r="17"/><ellipse cx="21" cy="21" rx="7" ry="17"/><path d="M4 21h34M7 12h28M7 30h28"/></svg>
    <h3>QUISQUE TEMPOR AUGUE</h3>
    <p>Donec vitae rhoncus ex. Nulla porttitor, ligula id suscipit vestibulum, ex justo dapibus lectus, in scelerisque ligula ex a lorem. Sed malesuada ultricies dui vitae accumsan.</p>
    <span class="more">MORE...</span>
  </div>
  <div class="abs feature" style="left:456px;top:758px">
    <svg width="42" height="42" viewBox="0 0 42 42" fill="none" stroke="#3cae3c" stroke-width="2"><rect x="8" y="4" width="26" height="34"/><path d="M13 14h16M13 20h16M13 26h10"/><path d="M22 32l4 4 8-10" /></svg>
    <h3>AUISQUE TEMPOR AUGUE</h3>
    <p>Donec vitae rhoncus ex. Nulla porttitor, ligula id suscipit vestibulum, ex justo dapibus lectus, in scelerisque ligula ex a lorem. Sed malesuada ultricies dui vitae accumsan.</p>
    <span class="more">MORE...</span>
  </div>
  <div class="abs feature" style="left:798px;top:758px">
    <svg width="42" height="42" viewBox="0 0 42 42" fill="none" stroke-width="3"><circle cx="21" cy="21" r="18" stroke="#222"/><path d="M12 21l6 6 12-12" stroke="#3cae3c"/></svg>
    <h3>TUISQUE TEMPOR AUGUE</h3>
    <p>Donec vitae rhoncus ex. Nulla porttitor, ligula id suscipit vestibulum, ex justo dapibus lectus, in scelerisque ligula ex a lorem. Sed malesuada ultricies dui vitae accumsan.</p>
    <span class="more">MORE...</span>
  </div>
</section>

<section class="gallery">
  <h2 class="abs section-title" style="top:1055px">NULLA ELEMENTUM LIGAOREET</h2>
  <p class="abs section-sub" style="top:1106px;font-size:14px;color:#333">Morbi tristique semper sem vel luctus. Ut dui augue,<br>suscipit vitae metus ut</p>
  <div class="abs tile" style="left:106px;top:1180px;width:304px;height:213px" role="img" aria-label="Microlight trike parked by a hangar"></div>
  <div class="abs tile" style="left:106px;top:1409px;width:304px;height:212px" role="img" aria-label="Powered hang glider on an airfield"></div>
  <div class="abs tile" style="left:424px;top:1180px;width:366px;height:441px" role="img" aria-label="Two-seat powered hang glider taking off"></div>
  <div class="abs tile" style="left:801px;top:1180px;width:304px;height:213px" role="img" aria-label="Microlight with orange wing on a runway apron"></div>
  <div class="abs tile" style="left:801px;top:1409px;width:304px;height:212px" role="img" aria-label="Powered hang glider on an airfield"></div>
</section>

<section class="about">
  <div class="abs about-photo" role="img" aria-label="Company team standing together"></div>
  <h2 class="abs about-label">ABOUT US</h2>
  <h3 class="abs about-head">AULLA ELEMENTUM LIGAET</h3>
  <p class="abs about-text" style="top:1875px">Donec vitae rhoncus ex. Nulla porttitor, ligula id suscipit vestibulum, ex justo dapibus lectus, in scelerisque ligula ex a lorem. Semalesua da ultricies dui vitae accumsan.</p>
  <p class="abs about-text" style="top:1954px">a porttitor, ligula id suscipit vestibulum, ex justo dapibus lectus, in scelerisque ligula ex a lorem. Semalesua da ultricies dui vitae accumsan.</p>
</section>

<section>
  <div class="abs testimonials"></div>
  <h2 class="abs t-title">TESTIMONIALS</h2>
  <div class="abs t-rule"></div>
  <div class="abs quote-mark" style="left:112px">&ldquo;</div>
  <div class="abs quote-mark" style="left:1052px">&rdquo;</div>
  <p class="abs t-quote">Morbi tristique semper sem vel luctus. Ut dui augue, suscipit vitae metus ut, tincidunt mollis tellus. Suspendisse ipsumMorbi tristique semper sem vel luctus. Ut dui augue, suscipit vitae metus ut, tincidunt mollis tellus. Suspendisse ipsum</p>
  <div class="abs t-name">Evan Marsh</div>
  <div class="abs t-role">CEO of Loft Co</div>
  <span class="abs dot" style="left:592px;border:2px solid #ccc"></span>
  <span class="abs dot" style="left:608px;background:var(--gold)"></span>
</section>

<section>
  <h2 class="abs news-label">Subscribe Our <strong>News Letter</strong></h2>
  <div class="abs news-input"></div>
  <div class="abs news-btn">submit</div>
</section>

<footer>
  <div class="abs footer"></div>
  <h4 class="abs f-head" style="left:147px">ABOUT US</h4>
  <h4 class="abs f-head" style="left:482px">INFORMATION</h4>
  <h4 class="abs f-head" style="left:817px">HARROW WORKS OFFICE</h4>

  <div class="abs f-brand"><span class="mark"></span>HARROW WORKS</div>
  <p class="abs f-about">Nullam tempor dui eget purus rhoncus, at efficitu Nullam tempor dui eget purus rhoncus, at efficitu</p>
  <div class="abs f-social"><span></span><span></span><span></span><span></span><span></span><span></span><span></span></div>

  <ul class="abs f-list" style="left:482px;top:2656px">
    <li>Home</li><li>Projects</li><li>Certifications</li><li>Core Values</li><li>Our Partners</li>
  </ul>
  <ul class="abs f-list" style="left:637px;top:2656px">
    <li>Company</li><li>Contact</li><li>Company History</li><li>FAQ</li><li>Our Team</li>
  </ul>

  <ul class="abs f-contact">
    <li><svg width="12" height="14" viewBox="0 0 12 14"><path d="M6 0a5 5 0 0 1 5 5c0 4-5 9-5 9S1 9 1 5a5 5 0 0 1 5-5z" fill="#bbb"/><circle cx="6" cy="5" r="2" fill="#231f20"/></svg>Nullam tempor dui eget purus rhoncus</li>
    <li><svg width="12" height="12" viewBox="0 0 12 12"><path d="M2 0l3 3-1.5 2a7 7 0 0 0 3.5 3.5L9 7l3 3-2 2C5 12 0 7 0 2z" fill="#bbb"/></svg>(555) 014 2231</li>
    <li><svg width="13" height="10" viewBox="0 0 13 10"><rect width="13" height="10" fill="#bbb"/><path d="M0 0l6.5 5L13 0" stroke="#231f20" fill="none"/></svg>info@brisktern.com</li>
    <li><svg width="13" height="12" viewBox="0 0 13 12"><rect y="3" width="13" height="9" fill="#bbb"/><rect x="3" width="7" height="4" fill="#bbb"/></svg>(555) 014 2290</li>
    <li><svg width="12" height="12" viewBox="0 0 12 12"><circle cx="6" cy="6" r="5.5" fill="#bbb"/><path d="M6 3v3h3" stroke="#231f20" fill="none"/></svg>Mon - Sat: 9:00 - 18:00</li>
  </ul>

  <p class="abs copyright">copyright2015-2016 Allrights reserve brisktern.com</p>
</footer>

</body>
</html>
```